Calmwell Learning - Wordpress Design Project

*IMPORTANT UPDATE*

The new Wordpress theme will be based on the Corvale Institute website templates (attached: http://www.pitchloom.com.au/file.aspx?fileLocation=storage_url/brief_uploads/74826_universitystandardwebtemplate_320_brief135807.zip).

Please do not take the design of the old Wordpress theme into account. The logo, icons, graphics from the old Wordpress theme are not to be used in your design.

1. Project overview

We need a customised wordpress theme and need to update the existing website www.calmwelllearning.edu.au using the Corvale Institute branding components such as logo, colours, text sizes, fonts, table styles etc.

2. Project aim

We would like the new website to make more online marketing sense. That is, we would like to increase student enrolment by improving the information on the website. Therefore, the new website needs to quickly communicate to the first time audience that: (1) this is a website from Corvale Institute, (2) this web site offers a self-paced multimedia e-learning course in Anxiety Disorders, (3) this course is accredited by professional organisations and supported by the Australian Government, (4) the course is lectured by 21 experts, (5) the price is AU$400 for 6 month access and AU$200 for extension for another 6 months, (6) users can sign up for the course online and get immediate access, (7) the benefits of learning the course, (8) the learning outcome, and (9) users can access to a lot of information for free on the website (this is to be done in two ways - the new website will have a blog, and it will offer a free ebook which the users can get via e-mail - they need to supply their first name and e-mail address).

3. Branding examples

The following are examples of different websites that apply the brand styles:

http://openhall.corvale.edu.au

http://big-questions.corvale.edu.au

http://mba.corvale.edu.au

http://inkbranch.corvale.edu.au

http://www.library.cvin.edu.au

http://blogs.cvin.edu.au/campusdays

http://corvale.edu.au/alumni/kit

4. Information to be used for the design of the new website:

(1) Information (e.g. text) from existing website: http://www.calmwelllearning.edu.au

(2) Information from course outline web pages:
http://pdl.corvale.edu.au/course/clmw

(3) Program flyer:
http://www.calmwelllearning.edu.au/info/wp-content/uploads/2012/03/CLHP-Flyer-3-pages.pdf

5. Things to have on the home page

The following components are something that I would suggest be included in the home page, but I would like to leave the freedom for designers to create:

(1) Menu

(2) E-Learning Portal Login form (pointing to http://www.calmwelllearning.edu.au/e-learning)

(3) Sign up button/link

(4) Information about accreditation

(5) Latest posts from the blog

(6) Free e-book opt in form - "Nine Ways Through Restless Worry" (we will use MailChimp to deliver the e-book to the e-mail address that audience submits)

(7) Information about lecturers

(8) Our Facebook Page, Twitter and Linked Group

6. Home page layout

I would like to see different layout styles and compare. The two extremes of the spectrum would be either something like this: http://www.clinicpath.com.au/ (very clean), or something more crowded like some of the examples above.

7. Attachments

Our University has some templates (including style sheets) for web designers to use. I'm also attaching a brand guideline for designer's information. I have some screenshots of the e-learning program that may be used in the design.
Updates

Dear all,

Thanks for your participation. I'm sending you some important updates:

The Corvale Institute website templates (attached: http://www.pitchloom.com.au/file.aspx?fileLocation=storage_url/brief_uploads/74826_universitystandardwebtemplate_320_brief135807.zip) should be used as a starting point for your design.

The new Wordpress theme should carry a strong Corvale Institute brand, utilising the "Grid of Ideas" framework. Please refer to Page 43, 49, 52, and 53 of the Corvale Institute brand identity document: http://www.pitchloom.com/file.aspx?fileLocation=storage_url/brief_uploads/74826_corvale_institute_brand_identity_brief131935.pdf

You may get inspired from the following websites:

http://mba.corvale.edu.au

http://kindle.corvale.edu.au/

Thanks a lot!

Further to the update yesterday, I just posted one more file containing some examples of possible heading design.

They are all examples of the "Grid of Ideas" design style (square matrix with logo). Our new website will need to apply this style as well.

Please download this file:

Please remember: when a prospect customer descides to sign up, they will have to go to this page http://pdl.cvin.edu.au/course/CLMW to process credit card payment. Therefore, the Wordpress design should connect to that payment page naturaly, without making people think they are going somewhere else.

Reason: Designers, thanks for your interest in this project. As per request, I have extended the deadline due to Christmas and New Year holiday. Happy New Year to all!

Target Market(s)

Target audiences are psychiatrists, psychologists, nurses, social workers, relationship therapists, teachers, counsellours etc. from all around the world

Industry/Entity Type

Marketing

Requirements
Must have
• Corvale Institute logo along with the blue square should be used.
Should not have
• Please do not take the design of the old Wordpress theme (http://www.CalmwellLearning.edu.au) into account. The logo, icons, graphics from the old Wordpress theme are not to be used in your design.

```html
<!DOCTYPE html>
<html lang="en">
<head>
<meta charset="utf-8">
<title>Calmwell Learning for Health Professionals</title>
<link rel="stylesheet" href="https://fonts.googleapis.com/css2?family=Open+Sans:ital,wght@0,400;0,600;0,700;1,400;1,600;1,700&family=Oswald:wght@400;500&display=swap">
<style>
:root{
  --gold:#f6b92b;
  --gold-light:#fde9b0;
  --red:#d42027;
  --navy:#1c3f6e;
  --navy-dark:#163459;
  --ink:#333;
  --grey-text:#666;
  --link:#2a5d9f;
  --footer:#eeeeee;
  --line:#d9d9d9;
}
*{box-sizing:border-box;margin:0;padding:0}
html,body{width:757px;height:1200px;overflow:hidden;background:#fff}
body{position:relative;font-family:"Open Sans",Arial,sans-serif;color:var(--ink)}
.abs{position:absolute}

/* top bar */
.topbar{left:0;top:0;width:757px;height:33px;background:#fff;border-bottom:1px solid #e5e5e5;display:flex;align-items:center;font-size:10px;font-weight:600;color:var(--navy)}
.unit-title{background:var(--gold);color:#fff;height:20px;line-height:20px;padding:0 14px;font-size:9px;letter-spacing:.3px}
.top-links a{color:var(--navy);text-decoration:none;padding:0 12px;border-left:1px solid var(--gold)}
.top-links a:first-child{border-left:none}
.site-search{left:522px;top:6px;width:233px;height:19px;border:1px solid var(--navy);display:flex;align-items:center;font-size:8px;font-style:italic;color:var(--navy)}
.site-search .drop{width:16px;height:17px;background:var(--navy)}
.site-search span{flex:1;padding-left:6px}
.site-search .go{width:18px;height:17px;background:var(--red)}

/* header */
.header-gold{left:223px;top:33px;width:534px;height:137px;background:var(--gold)}
.header-navy{left:75px;top:33px;width:148px;height:137px;background:var(--navy)}
.brand{left:0;top:33px;width:152px;height:72px;background:var(--red);display:flex;align-items:center;padding-left:14px;gap:8px;color:#fff;font-size:14px;font-weight:600;letter-spacing:.5px}
.brand .mark{width:14px;height:14px;background:#fff;flex:none}
.site-title{left:235px;top:72px;font-size:17.5px;line-height:32px;color:var(--navy-dark);letter-spacing:.2px;font-weight:400}
.login-field{left:547px;width:198px;height:18px;background:#fff;border:1px solid #e0a21d;font-size:9px;padding-left:6px;line-height:16px;color:#444}
.btn{height:19px;line-height:19px;font-size:9px;font-weight:700;color:#fff;padding:0 6px}
.btn-register{left:645px;top:107px;background:var(--navy)}
.btn-login{left:706px;top:107px;background:var(--red)}
.forgot{left:622px;top:136px;font-size:8px;color:var(--red)}

/* nav */
.main-nav{left:75px;top:170px;width:682px;height:37px;background:var(--gold-light);display:flex;padding-left:11px}
.main-nav a{font-size:12px;color:#333;text-decoration:none;padding:0 12px;line-height:37px;border-right:1px solid #f3d98e}
.main-nav a.active{background:var(--red);color:#fff}

.page-edge{left:75px;top:207px;width:1px;height:870px;background:#e5e5e5}
.page-edge.right{left:756px}

/* hero */
.hero{left:86px;top:218px;width:425px;height:238px;border:2px solid var(--gold);background:linear-gradient(90deg,#8a5a3a 0%,#3a2a22 45%,#111 75%)}
.hero-title{right:14px;top:12px;width:300px;text-align:right;font-family:"Oswald",sans-serif;font-size:17px;line-height:28px;color:var(--gold);white-space:nowrap}
.dots{right:14px;bottom:10px;display:flex;gap:6px}
.dots i{width:14px;height:14px;border-radius:50%;background:#fff;display:block}
.dots i:first-child{background:var(--gold)}

/* sections */
.sec-title{font-style:italic;font-weight:600;font-size:18px;color:var(--red)}
.sec-rule{height:1px;background:var(--navy)}
.read-more{font-size:8px;font-style:italic;font-weight:600;color:var(--navy);background:#fff;padding:0 6px}
.body-copy{font-size:9.4px;line-height:15.2px;color:var(--grey-text)}
.divider{height:1px;background:var(--line)}
.globe{left:414px;top:532px;width:92px;height:86px;border-radius:50%;background:radial-gradient(circle at 40% 40%,#7db8e8,#2a6fb0)}

/* sidebar */
.card-head{font-style:italic;font-weight:700;color:#fff;font-size:12.5px}
.posts{left:523px;top:218px;width:222px;height:197px;background:#e6e6e6;border:1px solid #ccc}
.posts-head{height:28px;background:var(--navy);padding:5px 10px}
.post{height:48px;border-bottom:1px solid #fff;display:flex;align-items:center;padding-left:10px;gap:5px}
.post .day{width:22px;height:24px;background:var(--navy);color:#fff;font-size:14px;text-align:center;line-height:24px}
.post .mon{font-size:7.5px;font-style:italic;font-weight:700;color:var(--navy);width:30px;line-height:11px}
.post .info{font-size:8px;line-height:12px;color:#444}
.post .info b{font-weight:400;color:var(--link)}
.posts-more{right:8px;bottom:6px;background:var(--red);color:#fff;font-size:7.5px;font-style:italic;font-weight:700;padding:2px 8px;border-radius:10px 0 0 0}

.ebook{left:523px;top:431px;width:222px;height:173px;background:var(--navy);border:2px solid #fff;outline:1px solid #ccc}
.ebook-head{height:43px;background:var(--gold);padding:4px 10px;line-height:16px}
.ebook-head .card-head{color:var(--navy-dark)}
.ebook-field{left:13px;width:196px;height:22px;background:#fff;border:1px solid #bbb;font-size:11px;padding-left:10px;line-height:20px;color:#222}
.subscribe{left:67px;bottom:0;width:90px;height:22px;background:var(--red);color:#fff;font-size:10px;font-weight:700;text-align:center;line-height:22px;letter-spacing:.6px;border-radius:10px 10px 0 0}

.testi-title{left:557px;top:622px;font-size:17px;font-style:italic;font-weight:600;color:var(--navy)}
.testi-photo{left:523px;top:646px;width:70px;height:114px;background:linear-gradient(160deg,#c8d8e8,#8aa5c0 60%,#2d4f7a)}
.testi-text{left:598px;top:647px;width:142px;font-size:7.6px;line-height:12.1px;color:#222}
.testi-more{left:646px;top:741px;font-size:8px;font-style:italic;font-weight:700;color:var(--red)}

/* footer */
.footer{left:75px;top:1076px;width:682px;height:108px;background:var(--footer)}
.social{left:86px;top:1091px;display:flex;gap:10px}
.social i{width:31px;height:31px;border-radius:50%;background:#dfe3ea;border:2px solid #fff;box-shadow:0 0 0 1px #c5cbd5;display:block}
.social i:first-child{background:var(--navy)}
.foot-links{left:86px;top:1154px;font-size:8.5px;color:var(--navy)}
.foot-links span{color:#999;padding:0 3px}
.foot-info{right:12px;top:1090px;text-align:right;font-size:8.5px;line-height:16.8px;color:#444}
.foot-info b{color:var(--navy);font-weight:600}
</style>
</head>
<body>

<div class="abs topbar">
  <span class="unit-title">UNIT TITLE</span>
  <nav class="top-links" style="padding-left:4px"><a>UNIVERSITY HOME</a><a>CONTACTS</a><a>SITEMAP</a></nav>
</div>
<div class="abs site-search"><i class="drop"></i><span>All university websites...</span><i class="go"></i></div>

<div class="abs header-gold"></div>
<div class="abs header-navy"></div>
<div class="abs brand"><i class="mark"></i>CORVALE INSTITUTE</div>
<h1 class="abs site-title">CALMWELL LEARNING FOR<br>HEALTH PROFESSIONALS (CLHP)</h1>
<div class="abs login-field" style="top:48px">Username:</div>
<div class="abs login-field" style="top:78px">Password:</div>
<div class="abs btn btn-register">REGISTER</div>
<div class="abs btn btn-login">LOGIN</div>
<div class="abs forgot">Forgot username or password ?</div>

<nav class="abs main-nav">
  <a class="active">About</a><a>Web</a><a>Print</a><a>Branding</a><a>Writing &amp; editing</a><a style="border:none">Style guides</a>
</nav>

<div class="abs page-edge"></div>
<div class="abs page-edge right"></div>

<div class="abs hero" role="img" aria-label="Photo of a student reading a book outdoors">
  <div class="abs hero-title">CLHP: ONLINE CONTINUING<br>PROFESSIONAL DEVELOPMENT<br>COURSE IN ANXIETY DISORDERS</div>
  <div class="abs dots"><i></i><i></i><i></i><i></i></div>
</div>

<!-- What is -->
<h2 class="abs sec-title" style="left:86px;top:482px">What is CLHP?</h2>
<div class="abs divider" style="left:86px;top:512px;width:425px"></div>
<p class="abs body-copy" style="left:87px;top:520px;width:320px;text-align:justify">The Calmwell Learning for Health Professionals (CLHP) is a self-paced online course collaboratively designed by 21 academics, clinicians and educators from 12 universities and hospitals across Australia and New Zealand to give a detailed introduction to the epidemiology, aetiology, clinical presentation, assessment, theoretical models, psychological and pharmacological management for anxiety disorders.</p>
<div class="abs globe" role="img" aria-label="E-learning globe illustration"></div>

<!-- Enrolment -->
<div class="abs divider" style="left:86px;top:650px;width:425px;background:#eee"></div>
<h2 class="abs sec-title" style="left:85px;top:660px">Enrolment</h2>
<div class="abs sec-rule" style="left:180px;top:673px;width:331px"></div>
<span class="abs read-more" style="left:433px;top:667px">Read more</span>
<p class="abs body-copy" style="left:85px;top:692px;width:426px">The enrolment procedure of CLHP is very simple and can be completed online in 10 minutes in most cases following these steps: (1) register personal details in our enrolment portal, (2) pay by credit card online, (3) receive an enrolment confirmation e-mail, and (4) use the credentials in the confirmation e-mail to log in to our e-learning portal. Alternatively, you can enrol by phone, post, fax, or in person.</p>

<!-- Accreditation -->
<div class="abs divider" style="left:86px;top:788px;width:425px;background:#eee"></div>
<h2 class="abs sec-title" style="left:85px;top:797px">Accreditation</h2>
<div class="abs sec-rule" style="left:203px;top:810px;width:308px"></div>
<span class="abs read-more" style="left:433px;top:804px">Read more</span>
<p class="abs body-copy" style="left:85px;top:829px;width:426px">CPD accreditation for CLHP has been awarded with a number of specialist colleges and professional associations in the health care field. Those participants who successfully complete the course will be issued a Certificate of Achievement or a Certificate of Participation depending on their scores in the final examination. With either certificate, participants may be able to claim up to 24 CPD hours.</p>

<!-- Lecturers -->
<div class="abs divider" style="left:86px;top:925px;width:425px;background:#eee"></div>
<h2 class="abs sec-title" style="left:85px;top:934px">Lecturers</h2>
<div class="abs sec-rule" style="left:170px;top:947px;width:341px"></div>
<span class="abs read-more" style="left:433px;top:941px">Read more</span>
<p class="abs body-copy" style="left:85px;top:966px;width:426px">CPD accreditation for CLHP has been awarded with a number of specialist colleges and professional associations in the health care field. Those participants who successfully complete the course will be issued a Certificate of Achievement or a Certificate of Participation depending on their scores in the final examination. With either certificate, participants may be able to claim up to 24 CPD hours.</p>

<!-- Recent posts -->
<aside class="abs posts">
  <div class="posts-head"><span class="card-head">Recent Posts</span></div>
  <div class="post" style="margin-top:4px"><span class="day">01</span><span class="mon">Jan<br>2013</span><span class="info"><b>Lorem ipsum dolor sit amet lorem</b><br>Time: 6:00 PM<br>Location: Harlow Hall</span></div>
  <div class="post"><span class="day">06</span><span class="mon">Jan<br>2013</span><span class="info"><b>Lorem ipsum dolor sit ametlo</b><br>Time: 6:00 PM<br>Location: Harlow Hall</span></div>
  <div class="post" style="border:none"><span class="day">10</span><span class="mon">Jan<br>2013</span><span class="info"><b>Lorem ipsum dolor sit ametlorem</b><br>Time: 6:00 PM<br>Location: Harlow Hall</span></div>
  <span class="abs posts-more">Read More...</span>
</aside>

<!-- Ebook -->
<aside class="abs ebook">
  <div class="ebook-head"><span class="card-head">Nine Ways Through<br>Restless Worry</span></div>
  <div class="abs ebook-field" style="top:61px">Name:</div>
  <div class="abs ebook-field" style="top:105px">Email Address:</div>
  <div class="abs subscribe">SUBSCRIBE</div>
</aside>

<!-- Testimonials -->
<svg class="abs" style="left:526px;top:628px" width="22" height="16" viewBox="0 0 22 16" aria-hidden="true"><path d="M2 14c0-6 3-10 8-12M11 14c0-6 3-10 8-12" stroke="#1c3f6e" stroke-width="3" fill="none"/></svg>
<h2 class="abs testi-title">Testimonials</h2>
<div class="abs testi-photo" role="img" aria-label="Portrait of a smiling course graduate"></div>
<svg class="abs" style="left:592px;top:640px" width="155" height="122" viewBox="0 0 155 122" aria-hidden="true">
  <path d="M60 1H153V101H132L120 118L124 101H2" fill="none" stroke="#1c3f6e" stroke-width="2"/>
</svg>
<p class="abs testi-text">Lorem ipsum dolor sit amet, ctetur adipiscing elit. Integer lorem ante, pellentesque a accumsan a, iaculis in risus. Morbi sed justo vitae ortor rutrum pharetra. Integer sit amet mauris eget nisl dapibus Lorem ipsum dolor sit amet.</p>
<span class="abs testi-more">View More...</span>

<!-- Footer -->
<footer class="abs footer"></footer>
<div class="abs social" aria-label="Social media links"><i></i><i></i><i></i><i></i></div>
<div class="abs foot-links">Contact the University<span>/</span>Disclaimer<span>/</span>Privacy<span>/</span>Accessibility</div>
<div class="abs foot-info">
  © 2002-13 The Corvale Institute.<br>
  <b>Last updated:</b> 04 January 2013<br>
  <b>ABN:</b> 48 302 716 095. CRICOS number: 00419K.<br>
  <b>Phone:</b> +61 2 9000 4100<br>
  Authorised by: Director, Marketing and Communications.
</div>

</body>
</html>
```